Product Label & Logo for New Supplement

Your design will automatically be eliminated if you do NOT read this brief, because the description tells you about the brand you will be creating an identity for.Attached is the current label for the product. It is boring and doesn’t tell a story.We need you to unleash creative work to help patients with chronic pain diseases - like Multiple Sclerosis, Chronic Fatigue Syndrome, Lupus, and Fibromyalgia - no longer be defined by their disease. Velq Tonic is a new supplement developed by a neurologist to help patients with chronic pain feel better and have better days. It increases energy and stamina, saving the patient from having to take upwards of 40 different supplements.The label and logo need to convey that this supplement will give hurting patients new life.
Updates
Target Market(s)
People with fatigue, pain and inflammation
Industry/Entity Type
Supplement
Requirements
Must have
- Gender neutral, eye catching, all the ingredients listed in addition to logo design
Nice to have
- Custom logo, no generic fonts for name brand

```html
<!DOCTYPE html>
<html lang="en">
<head>
<meta charset="utf-8">
<title>Velq Tonic – Supplement Label</title>
<link href="https://fonts.googleapis.com/css2?family=Bebas+Neue&display=swap" rel="stylesheet">
<style>
  :root {
    --stage: #1e1e1e;
    --ink: #3a1673;
    --violet: #7b2fd4;
    --orchid: #b45ae6;
    --blue: #3f5ee2;
    --sky: #9cc0f4;
    --haze: #f2f5fc;
    --band: rgba(255, 255, 255, 0.62);
    --band-line: rgba(80, 48, 160, 0.7);
  }
  * { margin: 0; padding: 0; box-sizing: border-box; }
  html, body {
    width: 1200px;
    height: 787px;
    overflow: hidden;
    background: var(--stage);
  }
  .canvas {
    position: relative;
    width: 1200px;
    height: 787px;
    display: flex;
    justify-content: center;
  }
  .label {
    position: relative;
    width: 630px;
    height: 787px;
    overflow: hidden;
    font-family: "Bebas Neue", "Arial Narrow", sans-serif;
    color: var(--ink);
  }
  .label-artwork {
    position: absolute;
    inset: 0;
    background:
      radial-gradient(ellipse 22% 60% at 47% 62%, rgba(190, 100, 235, 0.95), rgba(190,100,235,0) 72%),
      radial-gradient(ellipse 18% 40% at 38% 88%, rgba(170, 70, 220, 0.95), rgba(170,70,220,0) 75%),
      radial-gradient(ellipse 16% 30% at 55% 12%, rgba(70, 90, 210, 0.9), rgba(70,90,210,0) 75%),
      radial-gradient(ellipse 36% 40% at 72% 62%, rgba(255,255,255,0.95), rgba(255,255,255,0) 70%),
      radial-gradient(ellipse 40% 30% at 80% 18%, rgba(150, 190, 245, 0.9), rgba(150,190,245,0) 70%),
      radial-gradient(ellipse 30% 40% at 5% 70%, rgba(130, 40, 210, 0.9), rgba(130,40,210,0) 75%),
      linear-gradient(120deg, var(--violet) 0%, #5a3fe0 25%, var(--blue) 42%, var(--sky) 65%, var(--haze) 82%, var(--orchid) 100%);
  }
  .brand-name {
    position: absolute;
    left: 32px;
    top: 326px;
    font-size: 110px;
    font-weight: 400;
    line-height: 1;
    letter-spacing: 19px;
    color: var(--ink);
    white-space: nowrap;
  }
  .info-band {
    position: absolute;
    left: 0;
    right: 0;
    top: 624px;
    height: 144px;
    background: var(--band);
  }
  .facts {
    position: absolute;
    left: 35px;
    top: 640px;
    font-size: 29px;
    line-height: 1;
  }
  .facts li { list-style: none; }
  .facts li:nth-child(1) { margin-bottom: 8px; }
  .facts li:nth-child(2) { margin-bottom: 20px; }
  .benefits {
    position: absolute;
    left: 420px;
    right: 0;
    top: 628px;
  }
  .benefits li {
    list-style: none;
    height: 50px;
    padding-left: 30px;
    display: flex;
    align-items: center;
    font-size: 22px;
    border-bottom: 3px solid var(--band-line);
  }
  .benefits li:last-child { border-bottom: none; }
</style>
</head>
<body>
  <main class="canvas">
    <section class="label">
      <div class="label-artwork" role="img" aria-label="Glowing purple and blue DNA double helix rising through a bright sky with a faint perspective grid and floating particles"></div>
      <h1 class="brand-name">Velq Tonic</h1>
      <div class="info-band"></div>
      <ul class="facts">
        <li>Dietary</li>
        <li>Supplement</li>
        <li>60 Tablets</li>
      </ul>
      <ul class="benefits">
        <li>Promotes Energy</li>
        <li>Decreases Pain</li>
        <li>Relieves Inflammation</li>
      </ul>
    </section>
  </main>
</body>
</html>
```